IT Services company general flyer

Looking for a printable US letter size flyer to give a brief overview of the services we offer. We also partner with another company for their services as well. Please check out our website at www.gizmobykellan.com and click on "Our Services" to learn about our services and visit www.bluefernguard,com and click on services to learn about their services. Several of our services do overlap, so they only need to be on the flyer once. Let me know if this is too much content and we need to weed some out. We do not want Home phone service on this flyer. The basic design of the flyer should mimic similar to the VOIP one you did for me for the colors and logo. Also check out the "Who Choose us" page on www.gizmobykellan.com to include some of that as well.

Target Market(s)

Targeting Small businesses that may not normally have a budget for their IT Services

Industry/Entity Type

It Service

Font styles to use
Serif
Sans Serif

Requirements
Must have
• Must include my logo, phone number and email/website address and must follow the same basic template of my previous flyers.

```html
<!DOCTYPE html>
<html lang="en">
<head>
<meta charset="utf-8">
<title>Gizmo By Kellan – IT Services Flyer</title>
<link href="https://fonts.googleapis.com/css2?family=Open+Sans:wght@600;700;800&family=Barlow:wght@300;400&display=swap" rel="stylesheet">
<style>
  :root{
    --navy:#1b2c5a;
    --navy-deep:#142247;
    --red:#b0242a;
    --red-dark:#8e1b1d;
    --teal-dark:#0c3142;
    --teal-mid:#1a5c75;
    --teal-light:#2b86a3;
    --band:#e7e8ea;
    --ink:#111;
    --body:#444;
    --white:#fff;
  }
  *{margin:0;padding:0;box-sizing:border-box}
  html,body{width:969px;height:1200px;overflow:hidden;background:var(--white)}
  .flyer{position:relative;width:969px;height:1200px;overflow:hidden;background:var(--white);font-family:"Barlow",sans-serif}
  .backdrop{position:absolute;left:0;top:0}
  .brand{position:absolute;left:566px;top:62px;display:flex;align-items:center;gap:16px}
  .brand-dot{width:62px;height:62px;border-radius:50%;background:var(--navy)}
  .brand-name{font-family:"Open Sans",sans-serif;font-weight:700;color:var(--navy);font-size:34px;line-height:36px;letter-spacing:-.5px}
  .services{position:absolute;left:0;top:0;color:var(--white)}
  .services-title{position:absolute;left:47px;top:436px;font-family:"Open Sans",sans-serif;font-weight:600;font-size:33px;white-space:nowrap}
  .rule{position:absolute;left:47px;height:2px;background:var(--white)}
  .rule.short{top:500px;width:242px}
  .rule.long{top:586px;width:318px}
  .services-intro{position:absolute;left:47px;top:510px;width:330px;font-family:"Open Sans",sans-serif;font-weight:700;font-size:15px;line-height:20px}
  .service{position:absolute;left:46px;width:430px}
  .service-icon{position:absolute;left:0;top:0;width:66px;height:66px;border-radius:50%;background:var(--red);display:flex;align-items:center;justify-content:center}
  .service-icon svg{width:38px;height:38px;fill:none;stroke:var(--white);stroke-width:2.2;stroke-linecap:round;stroke-linejoin:round}
  .service-name{position:absolute;left:82px;top:-2px;font-family:"Open Sans",sans-serif;font-weight:600;font-size:22.5px;line-height:30px;white-space:nowrap}
  .service-text{position:absolute;left:82px;top:30px;width:330px;font-size:11.5px;line-height:15px;font-weight:400;color:#e6e9f2}
  .why{position:absolute;left:532px;top:646px;width:394px}
  .why-title{font-family:"Open Sans",sans-serif;font-weight:800;color:var(--red-dark);font-size:35px;line-height:43px;margin-bottom:14px}
  .why h3{font-family:"Open Sans",sans-serif;font-weight:600;color:var(--ink);font-size:19.5px;line-height:24px;margin-bottom:9px}
  .why p{font-size:12.8px;line-height:16.6px;color:var(--body);font-weight:300;text-align:justify;margin-bottom:11px}
  .band{position:absolute;left:0;top:1088px;width:969px;height:53px;background:var(--band)}
  .phone{position:absolute;left:53px;top:1092px;display:flex;align-items:center;gap:8px;color:var(--red-dark);font-family:"Open Sans",sans-serif;font-weight:800;font-size:32px}
  .phone svg{width:30px;height:30px;fill:none;stroke:var(--red-dark);stroke-width:2.4}
  .web{position:absolute;left:524px;top:1095px;color:var(--red-dark);font-family:"Open Sans",sans-serif;font-weight:800;font-size:27px;white-space:nowrap}
  .mail-strip{position:absolute;left:0;top:1141px;width:484px;height:59px;background:var(--navy-deep)}
  .mail{position:absolute;left:58px;top:1154px;display:flex;align-items:center;gap:14px;color:var(--white);font-size:19px;font-family:"Open Sans",sans-serif;font-weight:600}
  .mail svg{width:24px;height:18px;fill:#cfd4e0}
</style>
</head>
<body>
<div class="flyer">
  <svg class="backdrop" width="969" height="1200" viewBox="0 0 969 1200">
    <defs>
      <radialGradient id="techGlow" cx="0.62" cy="0.55" r="0.6">
        <stop offset="0" stop-color="#2b86a3"/>
        <stop offset="0.55" stop-color="#1a5c75"/>
        <stop offset="1" stop-color="#0c3142"/>
      </radialGradient>
      <linearGradient id="panelShade" x1="0" y1="0" x2="0" y2="1">
        <stop offset="0" stop-color="#1f3266"/>
        <stop offset="1" stop-color="#142247"/>
      </linearGradient>
    </defs>
    <path role="img" aria-label="Abstract digital technology background with circular interface rings and binary code"
      d="M0 0 L245 0 C420 80 650 190 804 204 C880 210 930 180 969 150 L969 525 C900 565 820 632 724 636 C640 640 560 610 472 544 L0 700 Z"
      fill="url(#techGlow)"/>
    <path d="M245 0 C420 80 650 190 804 204 C880 210 930 180 969 150" fill="none" stroke="var(--red)" stroke-width="6"/>
    <path d="M472 544 C560 610 640 640 724 636 C820 632 900 565 969 525" fill="none" stroke="var(--red)" stroke-width="7"/>
    <path d="M0 257 C200 350 340 405 400 445 C460 485 484 540 484 600 L484 1088 L0 1088 Z" fill="url(#panelShade)"/>
  </svg>

  <div class="brand">
    <div class="brand-dot"></div>
    <div class="brand-name">GIZMO<br>BY KELLAN</div>
  </div>

  <section class="services">
    <h2 class="services-title">Our Services</h2>
    <div class="rule short"></div>
    <p class="services-intro">We provide a complete range of IT services focused on you getting the most from your technology.</p>
    <div class="rule long"></div>

    <div class="service" style="top:601px">
      <div class="service-icon"><svg viewBox="0 0 40 40"><rect x="5" y="6" width="30" height="22" rx="2"/><path d="M12 34l4-6M12 11l16 14M28 11L12 25"/></svg></div>
      <h3 class="service-name">MANAGED IT SERVICES</h3>
      <p class="service-text">You need your IT systems for your day to day work. Let us help manage and protect them.</p>
    </div>
    <div class="service" style="top:678px">
      <div class="service-icon"><svg viewBox="0 0 40 40"><path d="M9 12c0 10 8 19 19 20l3-5-6-3-3 3c-4-2-7-5-9-9l3-3-3-6z"/><rect x="22" y="6" width="14" height="10" rx="2"/></svg></div>
      <h3 class="service-name">Business VOIP</h3>
      <p class="service-text">Reduce cost and improve communication for your business. Solutions available for any size business from 1 phone to hundreds of phones.</p>
    </div>
    <div class="service" style="top:758px">
      <div class="service-icon"><svg viewBox="0 0 40 40"><rect x="5" y="7" width="22" height="7" rx="2"/><rect x="5" y="17" width="16" height="7" rx="2"/><rect x="5" y="27" width="16" height="7" rx="2"/><path d="M30 18l6 2v6c0 4-3 7-6 8-3-1-6-4-6-8v-6z"/><path d="M27 26l2 2 4-4"/></svg></div>
      <h3 class="service-name">NETWORK SECURITY</h3>
      <p class="service-text">Worried about the latest ransomware or crypto virus? We can help design and protect your network.</p>
    </div>
    <div class="service" style="top:838px">
      <div class="service-icon"><svg viewBox="0 0 40 40"><rect x="6" y="12" width="22" height="14" rx="2"/><path d="M28 16l7-4v14l-7-4"/><path d="M14 26v6M9 32h10"/></svg></div>
      <h3 class="service-name">SECURITY CAMERAS</h3>
      <p class="service-text">With our partner Blue Fern Guard we install camera, alarm and access control systems to keep your site safe.</p>
    </div>
    <div class="service" style="top:918px">
      <div class="service-icon"><svg viewBox="0 0 40 40"><rect x="6" y="24" width="28" height="9" rx="2"/><path d="M10 24l-3-6M30 24l3-6M12 15a11 11 0 0 1 16 0M15 19a6 6 0 0 1 10 0M24 28h1M28 28h1"/></svg></div>
      <h3 class="service-name">WIRELESS SOLUTIONS</h3>
      <p class="service-text">Is your wireless coverage spotty or would you like to extend your network or internet coverage to another building?</p>
    </div>
    <div class="service" style="top:998px">
      <div class="service-icon"><svg viewBox="0 0 40 40"><path d="M11 24a7 7 0 0 1 1-13 9 9 0 0 1 17 2 6 6 0 0 1 0 11z"/><path d="M14 24v6M20 24v8M26 24v6"/><circle cx="14" cy="32" r="2"/><circle cx="20" cy="34" r="1.5"/><circle cx="26" cy="32" r="2"/></svg></div>
      <h3 class="service-name">CLOUD SERVICES</h3>
      <p class="service-text">Want your own business email service? Want to move to the cloud for secure file storage and sharing? Ask us about our cloud services.</p>
    </div>
  </section>

  <section class="why">
    <h2 class="why-title">Why Choose Gizmo By Kellan?</h2>
    <h3>Personalized Solutions and Support</h3>
    <p>We know your time is valuable and your technology is critical. That's why we take time to visit with each of our clients and recommend the best solution for them. Your not just another client to us, we want what is best for you.</p>
    <h3>Experience</h3>
    <p>We have years of experience in both large and small environments. We know what solutions are available and how to implement them in your business. We are constantly working with industry experts with today's changing technology.</p>
    <h3>One Stop Shop</h3>
    <p>We can help you with all your IT needs, weather it be computer or network security. Phone and Voice needs, or cloud services. Contact us today to discuss how we can help you.</p>
  </section>

  <div class="band"></div>
  <div class="phone">
    <svg viewBox="0 0 30 30"><circle cx="15" cy="15" r="12"/><path d="M10 9c0 6 5 11 11 11l1-3-3-2-2 2c-2-1-3-2-4-4l2-2-2-3z" fill="var(--red-dark)" stroke="none"/></svg>
    <span>555.014.2276</span>
  </div>
  <div class="web">www.gizmobykellan.com</div>
  <div class="mail-strip"></div>
  <div class="mail">
    <svg viewBox="0 0 24 18"><path d="M0 0h24v3l-12 7L0 3z"/><path d="M0 5l12 7 12-7v13H0z"/></svg>
    <span>sales@gizmobykellan.com</span>
  </div>
</div>
</body>
</html>
```